Business Card Design for a Lending Business (Hard Money loans)

We need a business card for our Real Estate Lending business. We do hard Money loans for real estate investors. We have an existing logo we like, see attached. I'd like the business card to mostly include the logo colors, but a bright color pop of some sort would be nice to see also. Card should include Logo, Company Name, Company Address, Employee Name, Cell Phone, Main Phone, Email, Website

Industry/Entity Type

Finance / Lending

Contact Information for Business Card

Logo, Company Name, Company Address, Employee Name, Cell Phone, Main Phone, Email, Website

Requirements
Nice to have
• I'd like the business card to mostly include the logo colors, but a bright color pop of some sort would be nice to see also.

```html
<!DOCTYPE html>
<html lang="en">
<head>
<meta charset="utf-8">
<title>Corridor Lending – Business Card</title>
<link href="https://fonts.googleapis.com/css2?family=Montserrat:wght@400;500;700;800&display=swap" rel="stylesheet">
<style>
  :root {
    --backdrop: #2b2b2d;
    --card: #ffffff;
    --card-shade: #ececec;
    --navy: #22307f;
    --sky: #1ba8dd;
    --ink: #444448;
    --ghost: #dcdcdc;
    --rule: #8e92c2;
  }
  * { box-sizing: border-box; margin: 0; padding: 0; }
  html, body {
    width: 1200px; height: 900px; overflow: hidden;
    background: var(--backdrop);
    font-family: "Montserrat", sans-serif;
  }
  .canvas { position: relative; width: 1200px; height: 900px; }

  .card {
    position: absolute;
    width: 630px; height: 360px;
    background: linear-gradient(115deg, var(--card-shade) 0%, var(--card) 55%, var(--card) 100%);
    overflow: hidden;
    box-shadow: 0 14px 30px rgba(0,0,0,.45);
  }
  .card--front { left: 140px; top: 70px; }
  .card--back  { left: 430px; top: 480px; }

  .ghost-disc {
    position: absolute;
    border-radius: 50%;
    background: var(--ghost);
    opacity: .55;
  }
  .card--front .ghost-disc { width: 360px; height: 360px; left: -40px; top: 80px; }
  .card--back  .ghost-disc { width: 330px; height: 330px; left: -10px; top: 90px; }

  .brand {
    position: absolute;
    display: flex; align-items: center; gap: 12px;
    color: var(--navy);
    font-weight: 800;
    text-transform: uppercase;
    letter-spacing: .08em;
    line-height: 1.05;
  }
  .brand__dot { border-radius: 50%; background: var(--navy); flex: none; }
  .card--front .brand { right: 56px; top: 96px; font-size: 34px; }
  .card--front .brand__dot { width: 44px; height: 44px; }
  .card--back .brand { right: 50px; top: 44px; font-size: 26px; }
  .card--back .brand__dot { width: 34px; height: 34px; }

  .person { position: absolute; left: 44px; top: 150px; }
  .person__name {
    font-size: 21px; font-weight: 800; text-transform: uppercase; letter-spacing: .01em;
  }
  .person__first { color: var(--navy); }
  .person__last { color: var(--sky); }
  .person__title { font-size: 15px; color: var(--ink); margin-top: 2px; }

  .contacts { position: absolute; left: 44px; top: 218px; list-style: none; }
  .contacts li {
    display: flex; align-items: center; gap: 12px;
    font-size: 14.5px; color: var(--ink); height: 21px;
  }
  .contacts svg { width: 15px; height: 15px; flex: none; }

  .divider {
    position: absolute; left: 44px; right: 90px; top: 318px;
    height: 1px; background: var(--rule);
  }
  .address {
    position: absolute; left: 44px; top: 326px;
    display: flex; align-items: center; gap: 12px;
    font-size: 14.5px; color: var(--ink);
  }
  .address svg { width: 15px; height: 18px; }
</style>
</head>
<body>
<main class="canvas">

  <section class="card card--front" aria-label="Card front">
    <div class="ghost-disc"></div>
    <div class="brand">
      <span class="brand__dot"></span>
      <span>Corridor<br>Lending</span>
    </div>
  </section>

  <section class="card card--back" aria-label="Card back">
    <div class="ghost-disc"></div>
    <div class="brand">
      <span class="brand__dot"></span>
      <span>Corridor<br>Lending</span>
    </div>

    <div class="person">
      <p class="person__name"><span class="person__first">Daniel</span> <span class="person__last">Marsh</span></p>
      <p class="person__title">CEO</p>
    </div>

    <ul class="contacts">
      <li>
        <svg viewBox="0 0 16 16" fill="none" stroke="var(--sky)" stroke-width="1.4"><rect x="4" y="1" width="8" height="14" rx="1.5"/><line x1="7" y1="12.5" x2="9" y2="12.5"/></svg>
        555-210-4471
      </li>
      <li>
        <svg viewBox="0 0 16 16" fill="var(--sky)"><path d="M3.5 1.5l2.3 2.6-1.2 1.6c.9 2 2.4 3.6 4.4 4.6l1.6-1.2 2.6 2.2-1.3 2.2C7 14.5 1.8 9.3 1.3 3.2z"/></svg>
        555-230-8812
      </li>
      <li>
        <svg viewBox="0 0 16 16" fill="var(--sky)"><path d="M1 3h14v10H1z"/><path d="M1 3l7 6 7-6" fill="none" stroke="#fff" stroke-width="1.3"/></svg>
        info@CorridorLending.com
      </li>
      <li>
        <svg viewBox="0 0 16 16" fill="none" stroke="var(--sky)" stroke-width="1.2"><circle cx="8" cy="8" r="6.5"/><ellipse cx="8" cy="8" rx="3" ry="6.5"/><line x1="1.5" y1="8" x2="14.5" y2="8"/></svg>
        www.corridorlending.com
      </li>
    </ul>

    <div class="divider"></div>

    <p class="address">
      <svg viewBox="0 0 14 18" fill="var(--sky)"><path d="M7 0a6 6 0 0 1 6 6c0 4.5-6 12-6 12S1 10.5 1 6a6 6 0 0 1 6-6z"/><circle cx="7" cy="6" r="2.3" fill="#fff"/></svg>
      1250 Harbor Lane, Millbrook, MD 20614
    </p>
  </section>

</main>
</body>
</html>
```